Marlow Hire Business Card for recruitment company

We are looking for a Business Card Design that incorporates our personal details and our busines name and logo. We are a specialized search consultancy that recruit Property and Construction professionals.
We would like a business card that stands out and is appealing to the Construction and Property industry as well.

Target Market(s)

people in the construction and property industry

Contact Information for Business Card

Business Name and logo

Font styles to use
Serif

Colors
0094D4
00A9DD
6FCCEA
C7EBF8
E9F6FB

Requirements
Must have
• Business name and logo as well as contact details
Should not have
• No photos of us please

```html
<!DOCTYPE html>
<html lang="en">
<head>
<meta charset="utf-8">
<title>Marlow Hire – Business Card</title>
<link rel="stylesheet" href="https://fonts.googleapis.com/css2?family=Montserrat:wght@300;400;600;700&display=swap">
<style>
  :root {
    --stage: #2a2d31;
    --card-dark: #1d1d1e;
    --teal: #0c4a60;
    --teal-deep: #053a4c;
    --teal-name: #0e5a76;
    --white: #ffffff;
    --soft-white: #e8e8e8;
    --orange: #f47b20;
  }
  * { box-sizing: border-box; margin: 0; padding: 0; }
  html, body {
    width: 1200px; height: 780px; overflow: hidden;
    background: var(--stage);
    font-family: "Montserrat", sans-serif;
  }
  .canvas { position: relative; width: 1200px; height: 780px; }

  .card {
    position: absolute; top: 235px;
    width: 540px; height: 310px;
    border-radius: 16px; overflow: hidden;
    box-shadow: 0 14px 30px rgba(0,0,0,.45);
  }

  /* Front */
  .card-front { left: 45px; background: var(--card-dark); }
  .edge-band { position: absolute; inset: 0; width: 100%; height: 100%; }
  .brand-name {
    position: absolute; left: 160px; top: 46px;
    font-size: 36px; font-weight: 300; letter-spacing: 2px;
    text-transform: uppercase; color: var(--white);
  }
  .contact-list {
    position: absolute; left: 52px; top: 128px;
    list-style: none;
  }
  .contact-list li {
    display: flex; align-items: center; gap: 10px;
    font-size: 12.5px; color: var(--soft-white);
    letter-spacing: .4px; height: 20px;
  }
  .contact-list svg { width: 13px; height: 13px; fill: var(--teal-name); }
  .divider {
    position: absolute; left: 48px; top: 202px;
    width: 440px; height: 1.5px; background: var(--white);
  }
  .address {
    position: absolute; left: 52px; top: 212px;
    display: flex; align-items: center; gap: 10px;
    font-size: 12.5px; color: var(--soft-white); letter-spacing: .4px;
  }
  .address svg { width: 13px; height: 13px; fill: var(--teal-name); }
  .person {
    position: absolute; right: 58px; top: 146px; text-align: right;
  }
  .person-name {
    font-size: 22px; font-weight: 700; color: var(--teal-name); letter-spacing: .8px;
  }
  .person-title {
    font-size: 13px; font-weight: 400; color: var(--white); letter-spacing: 1px;
    margin-top: 2px;
  }

  /* Back */
  .card-back { left: 615px; background: var(--teal); }
  .back-pattern {
    position: absolute; inset: 0;
    background: linear-gradient(135deg, #0d5069 0%, var(--teal) 50%, var(--teal-deep) 100%);
  }
  .back-brand {
    position: absolute; left: 0; right: 0; top: 186px; text-align: center;
    font-size: 24px; font-weight: 300; letter-spacing: 2px;
    text-transform: uppercase; color: var(--orange);
  }
</style>
</head>
<body>
<main class="canvas">

  <section class="card card-front" aria-label="Business card front">
    <svg class="edge-band" viewBox="0 0 540 310" preserveAspectRatio="none" aria-hidden="true">
      <polygon points="0,170 0,310 22,310 22,190" fill="var(--teal)"/>
      <polygon points="540,0 540,150 518,130 518,0" fill="var(--teal)"/>
    </svg>

    <h1 class="brand-name">Marlow Hire</h1>

    <ul class="contact-list">
      <li>
        <svg viewBox="0 0 24 24" aria-hidden="true"><path d="M6.6 10.8a15.1 15.1 0 0 0 6.6 6.6l2.2-2.2a1 1 0 0 1 1-.25 11.4 11.4 0 0 0 3.6.57 1 1 0 0 1 1 1V20a1 1 0 0 1-1 1A17 17 0 0 1 3 4a1 1 0 0 1 1-1h3.5a1 1 0 0 1 1 1c0 1.25.2 2.45.57 3.57a1 1 0 0 1-.25 1z"/></svg>
        041-552-7308
      </li>
      <li>
        <svg viewBox="0 0 24 24" aria-hidden="true"><path d="M2 5h20v14H2zm2 2v.5l8 5 8-5V7l-8 5z"/></svg>
        hello@marlowhire.com
      </li>
      <li>
        <svg viewBox="0 0 24 24" aria-hidden="true"><path d="M12 2a10 10 0 1 0 0 20 10 10 0 0 0 0-20zm6.9 9h-3a15 15 0 0 0-1.3-6A8 8 0 0 1 18.9 11zM12 4c.9 1.3 1.7 3.9 1.9 7h-3.8C10.3 7.9 11.1 5.3 12 4zM9.4 5a15 15 0 0 0-1.3 6h-3A8 8 0 0 1 9.4 5zM5.1 13h3a15 15 0 0 0 1.3 6 8 8 0 0 1-4.3-6zM12 20c-.9-1.3-1.7-3.9-1.9-7h3.8c-.2 3.1-1 5.7-1.9 7zm2.6-1a15 15 0 0 0 1.3-6h3a8 8 0 0 1-4.3 6z"/></svg>
        www.marlowhire.com
      </li>
    </ul>

    <div class="person">
      <p class="person-name">Daniel Reyes</p>
      <p class="person-title">General Manager</p>
    </div>

    <div class="divider"></div>

    <p class="address">
      <svg viewBox="0 0 24 24" aria-hidden="true"><path d="M12 2a7 7 0 0 0-7 7c0 5.2 7 13 7 13s7-7.8 7-13a7 7 0 0 0-7-7zm0 9.5A2.5 2.5 0 1 1 12 6.5a2.5 2.5 0 0 1 0 5z"/></svg>
      27 Harbour Row Bellmead, VA 20411
    </p>
  </section>

  <section class="card card-back" aria-label="Business card back">
    <div class="back-pattern" role="img" aria-label="Repeating brand pattern in dark teal tones"></div>
    <p class="back-brand">Marlow Hire</p>
  </section>

</main>
</body>
</html>
```